Redesign of Website

We need an overhaul of our website. I've attached our current logo files. Please visit www.pelvorix.com for our current website for information about our company. We are looking for the same type of website (information-based only) so no need for any online store, payments, interactive stuff or anything like that...basically looking for a fresh new look! Also please make sure this design will be mobile-friendly. Thanks!

```html
<!DOCTYPE html>
<html lang="en">
<head>
<meta charset="utf-8">
<title>Pelvorix Consultants</title>
<link href="https://fonts.googleapis.com/css2?family=Roboto:wght@400;500;700&family=Montserrat:wght@400;600&display=swap" rel="stylesheet">
<style>
  :root {
    --navy: #0a3282;
    --navy-deep: #0b2560;
    --navy-bottom: #0a1f52;
    --ink: #4a4f57;
    --heading: #0a2c6e;
    --logo-blue: #1d4f9c;
    --logo-grey: #57606b;
    --white: #ffffff;
  }
  * { box-sizing: border-box; margin: 0; padding: 0; }
  html, body { width: 992px; height: 1200px; overflow: hidden; background: var(--white); }
  body { font-family: "Roboto", Arial, sans-serif; position: relative; }

  .topbar {
    position: absolute; left: 0; top: 0; width: 992px; height: 29px;
    background: var(--navy); color: var(--white); font-size: 13px;
  }
  .topbar .call { position: absolute; left: 644px; top: 7px; }
  .topbar .locate { position: absolute; left: 852px; top: 7px; }

  .brand {
    position: absolute; left: 100px; top: 42px; width: 140px;
    font-weight: 700; color: var(--logo-blue); line-height: 1;
  }
  .brand .name { font-size: 30px; letter-spacing: 1px; }
  .brand .sub { font-size: 11.5px; letter-spacing: 2.4px; margin-top: 4px; }

  .mainnav {
    position: absolute; left: 271px; top: 51px; width: 721px; height: 49px;
    background: var(--navy); border-radius: 25px 0 0 25px;
    display: flex; gap: 9px; align-items: center; padding-left: 18px; padding-top: 6px;
  }
  .mainnav a { color: var(--white); text-decoration: none; font-weight: 700; font-size: 15.5px; letter-spacing: .3px; }

  .hero {
    position: absolute; left: 0; top: 119px; width: 992px; height: 337px;
    background: linear-gradient(100deg, #4f6680 0%, #7b6a58 35%, #8a6b52 55%, #35528a 85%, #1e3f88 100%);
  }
  .hero-caption {
    position: absolute; left: 0; top: 72px; width: 816px; height: 185px;
    background: rgba(18, 24, 36, 0.72); color: var(--white);
  }
  .hero-caption h2 { position: absolute; left: 134px; top: 34px; font-size: 23px; font-weight: 700; }
  .hero-caption p { position: absolute; left: 133px; top: 73px; width: 660px; font-size: 19.5px; line-height: 22.5px; }
  .hero .arrow { position: absolute; top: 144px; }
  .hero .arrow.prev { left: 18px; }
  .hero .arrow.next { left: 940px; }

  .about { position: absolute; left: 114px; top: 486px; width: 780px; color: var(--ink); }
  .about h1 { font-size: 20px; font-weight: 700; color: var(--heading); margin-bottom: 23px; }
  .about h1 .divider { color: var(--logo-grey); font-weight: 400; }
  .about p { font-size: 15.6px; line-height: 19px; letter-spacing: .15px; margin-bottom: 18px; }

  .band { position: absolute; left: 0; top: 920px; width: 992px; height: 17px; background: var(--navy); }

  .footer {
    position: absolute; left: 0; top: 951px; width: 992px; height: 204px;
    background: linear-gradient(180deg, var(--navy) 0%, var(--navy-deep) 100%);
    color: var(--white); font-family: "Montserrat", Arial, sans-serif; font-size: 14px;
  }
  .footer .foot-brand { position: absolute; left: 64px; top: 62px; color: #5d7db4; font-family: "Roboto", Arial, sans-serif; font-weight: 700; line-height: 1; }
  .footer .foot-brand .name { font-size: 31px; letter-spacing: 1px; }
  .footer .foot-brand .sub { font-size: 12px; letter-spacing: 2.3px; margin-top: 5px; }
  .footer .rule { position: absolute; top: 36px; width: 1px; height: 134px; background: #5a73a8; }
  .footer ul { list-style: none; position: absolute; line-height: 19.5px; }
  .footer .col-links { left: 309px; top: 57px; }
  .footer .col-info { left: 545px; top: 54px; }
  .footer .follow { position: absolute; left: 749px; top: 54px; }
  .footer .socials { display: flex; gap: 3px; margin-top: 5px; }
  .footer .socials span { width: 16px; height: 16px; border-radius: 3px; background: var(--white); display: block; }

  .copyright {
    position: absolute; left: 0; top: 1155px; width: 992px; height: 45px;
    background: var(--navy-bottom); color: #dfe5f2; font-size: 11.5px;
    text-align: center; line-height: 45px;
  }
</style>
</head>
<body>
  <div class="topbar">
    <span class="call">Call us now! 700 5550 142</span>
    <span class="locate">Find our Location</span>
  </div>

  <div class="brand">
    <div class="name">Pelvorix</div>
    <div class="sub">CONSULTANTS</div>
  </div>

  <nav class="mainnav">
    <a href="#">HOME</a><a href="#">ABOUT</a><a href="#">CONTACT</a><a href="#">SERVICE</a>
  </nav>

  <section class="hero" role="img" aria-label="Photo of a brick house under construction with scaffolding and a worker">
    <div class="hero-caption">
      <h2>Property Condition Reports</h2>
      <p>Before moving ahead on any loan approval, financial institutions need to know the condition of existing structures. Our professional staff will give you the details you need to make sound business decisions</p>
    </div>
    <svg class="arrow prev" width="24" height="32" viewBox="0 0 24 32"><polyline points="20,3 5,16 20,29" fill="none" stroke="#fff" stroke-width="3"/></svg>
    <svg class="arrow next" width="24" height="32" viewBox="0 0 24 32"><polyline points="4,3 19,16 4,29" fill="none" stroke="#fff" stroke-width="3"/></svg>
  </section>

  <main class="about">
    <h1>pelvorix.com – Pelvorix <span class="divider">|</span> Consultants</h1>
    <p>With over 25 years experience we provide customized and comprehensive inspection services to financial institution involved in construction and loan management in New York, New Jersey, Pennsylvania and surrounding areas.</p>
    <p>The firm’s professional staff bring years of engineering, environmental, building, and real estate experience to work for our clients.</p>
    <p>Pelvorix provides our clients with in-depth plan &amp; cost, construction funding, environmental and property condition reports.</p>
    <p>Pelvorix will give you the essential facts that are critical for solid business decision making and ongoing loan management.</p>
    <p>Pelvorix Consultants’ projects range from single family homes to $30,000,000 mid-rise buildings to $60,000,000 casino renovation projects. Our clients have come to think of us as part of their trusted team. They turn to us to evaluate plans, costs and approvals before they commit to a construction loan; and enlist our services throughout the construction process to ensure that all phases of the project are funded properly and documented accordingly. Pelvorix understands the delicate balance required in order to protect the client’s position and simultaneously keep their customers satisfied.</p>
  </main>

  <div class="band"></div>

  <footer class="footer">
    <div class="foot-brand">
      <div class="name">Pelvorix</div>
      <div class="sub">CONSULTANTS</div>
    </div>
    <div class="rule" style="left:288px"></div>
    <ul class="col-links"><li>Home</li><li>About</li><li>Contact</li><li>Services</li></ul>
    <div class="rule" style="left:508px"></div>
    <ul class="col-info"><li>Map</li><li>Address</li></ul>
    <div class="rule" style="left:715px"></div>
    <div class="follow">
      Follow Us
      <div class="socials"><span></span><span></span><span></span><span></span></div>
    </div>
  </footer>

  <div class="copyright">Copyright © 2019 | pelvorix.com | 418 Birchwood Ave #12 Lakeview, NJ 07000 | 973-555-0186</div>
</body>
</html>
```